New Web Design Project

We need a website design for a new company called Studio Pelican. We offer :
- language tutoring for scholars or adult learners
- and other educational services associated with the French language as
*online support
*and immersive language cards games as card match, dominos, puzzle and happy family cards. Studio pelican will provide immersive and playful support to all age language learners.

Target Market(s)

Parents, French educators (teachers, tutors), Language schools, students

Industry/Entity Type

Tutoring

Coding

Coded - Design and coding required

Number of Pages Required

4 page

Requirements
Must have
• Clean and elegant design. Pages should be balanced and elements pleasingly presented
• Three buckets structure

```html
<!DOCTYPE html>
<html lang="en">
<head>
<meta charset="utf-8">
<title>Studio Pelican – Language Tutoring</title>
<link href="https://fonts.googleapis.com/css2?family=Raleway:wght@400;500;600;700;800&family=Open+Sans:ital,wght@0,400;0,600;1,400&display=swap" rel="stylesheet">
<style>
:root{
  --gold:#e0ad4a;
  --plum:#a8426f;
  --ink:#222222;
  --text:#555555;
  --muted:#888888;
  --line:#e4e4e4;
  --soft:#f5f5f5;
  --card:#f4f4f4;
  --white:#ffffff;
}
*{margin:0;padding:0;box-sizing:border-box}
html,body{width:1200px;height:2769px;overflow:hidden;background:var(--white)}
body{font-family:"Open Sans",Arial,sans-serif;color:var(--text);position:relative}
a{color:inherit;text-decoration:none}

/* header */
.site-header{position:absolute;left:0;top:0;width:1200px;height:130px;background:var(--white)}
.brand{position:absolute;left:132px;top:32px;display:flex;align-items:center;gap:12px}
.brand-mark{width:34px;height:34px;border-radius:50%;background:var(--gold)}
.brand-name{font-family:"Raleway",sans-serif;font-weight:700;font-size:30px;line-height:32px;color:var(--plum);width:170px}
.top-contact{position:absolute;right:132px;top:26px;display:flex;align-items:center;gap:8px;font-size:13px;color:var(--muted)}
.top-contact b{color:var(--ink);font-weight:400}
.socials{display:flex;gap:5px;margin-left:8px}
.socials span{width:22px;height:22px;border-radius:50%;border:1.5px solid #4a7fc1;display:block}
.socials span:last-child{border-color:#d34b4b}
.main-nav{position:absolute;right:132px;top:86px;display:flex;font-family:"Raleway",sans-serif;font-size:12px;font-weight:500;color:var(--ink)}
.main-nav a{padding:0 22px;height:44px;line-height:20px;position:relative}
.main-nav a:last-child{padding-right:0}
.main-nav a.active{color:var(--plum)}
.main-nav a.active::after{content:"";position:absolute;left:0;right:0;bottom:0;height:3px;background:var(--plum)}

/* hero */
.hero{position:absolute;left:0;top:130px;width:1200px;height:510px}
.hero-photo{position:absolute;inset:0;background:linear-gradient(90deg,#c9c4bd 0%,#b7c6c8 30%,#e8ecee 55%,#f3f5f6 100%)}
.hero-copy{position:absolute;left:646px;top:130px;width:422px}
.hero-kicker{font-family:"Raleway",sans-serif;font-weight:700;font-size:16px;color:var(--gold);letter-spacing:.3px}
.hero-title{font-family:"Raleway",sans-serif;font-weight:800;font-size:42px;color:var(--ink);margin-top:12px;letter-spacing:.5px}
.hero-text{font-size:15px;line-height:33px;color:#444;margin-top:6px}
.btn-outline{display:inline-block;border:1.5px solid var(--plum);color:var(--plum);font-size:10px;font-weight:600;letter-spacing:.4px;padding:10px 14px}
.hero .btn-outline{margin-top:22px;background:rgba(255,255,255,.4)}
.hero-dots{position:absolute;left:984px;top:442px;display:flex;gap:13px}
.hero-dots span{width:12px;height:12px;border-radius:50%;border:1.5px solid #888;display:block}
.hero-dots span.on{background:var(--gold);border-color:var(--gold)}

/* section titles */
.section-title{font-family:"Raleway",sans-serif;font-weight:400;font-size:28px;color:var(--ink);text-align:center;letter-spacing:.3px}
.section-title b{font-weight:800}

/* services */
.services{position:absolute;left:0;top:640px;width:1200px;height:502px}
.services .section-title{position:absolute;top:66px;left:0;right:0}
.service-card{position:absolute;top:196px;width:297px;height:216px;background:var(--card);border:1px solid var(--line);text-align:center}
.service-icon{position:absolute;left:50%;top:-40px;width:80px;height:80px;margin-left:-40px;transform:rotate(45deg)}
.service-icon.gold{background:var(--gold)}
.service-icon.plum{background:var(--plum)}
.service-icon svg{transform:rotate(-45deg);width:80px;height:80px}
.service-card h3{font-family:"Raleway",sans-serif;font-weight:500;font-size:15px;color:var(--ink);margin-top:78px;letter-spacing:.3px}
.service-card p{font-size:10.5px;line-height:19.5px;color:#666;margin:10px 18px 0}
.more{display:inline-block;font-size:10px;color:var(--gold);margin-top:8px;letter-spacing:.3px}
.more.plum{color:var(--plum)}

/* tutoring band */
.tutoring{position:absolute;left:0;top:1142px;width:1200px;height:428px;background:var(--gold)}
.tutoring-title{position:absolute;left:132px;top:72px;font-family:"Raleway",sans-serif;font-weight:400;font-size:28px;color:var(--white);letter-spacing:.3px}
.tutoring-title b{font-weight:800}
.tick-list{position:absolute;left:132px;top:122px;width:412px;list-style:none}
.tick-list li{position:relative;padding-left:26px;font-size:10.5px;line-height:20px;color:var(--white);margin-bottom:20px}
.tick-list svg{position:absolute;left:0;top:4px}
.tutoring .btn-outline{position:absolute;left:132px;top:314px;border-color:var(--white);color:var(--white)}
.video{position:absolute;left:628px;top:78px;width:440px;height:272px;background:#1c1c1c}
.video-frame{position:absolute;left:0;top:0;width:440px;height:246px;background:linear-gradient(110deg,#5a6470 0%,#8d8f94 35%,#c7a98f 65%,#e9ddd2 100%)}
.video-play{position:absolute;left:190px;top:93px}
.video-bar{position:absolute;left:0;top:246px;width:440px;height:26px;background:var(--white)}

/* testimonials */
.testimonials{position:absolute;left:0;top:1570px;width:1200px;height:390px;background:var(--soft)}
.testimonials .section-title{position:absolute;top:70px;left:0;right:0}
.quote{position:absolute;top:140px;width:414px;padding-left:14px;border-left:1px solid #e6e6e6;height:170px}
.quote p{font-size:10.5px;line-height:20px;color:#555}
.quote p::before{content:"\201C";font-family:Georgia,serif;font-size:24px;color:var(--ink);vertical-align:-8px;margin-right:2px}
.author{position:absolute;left:26px;top:100px;display:flex;align-items:center;gap:26px}
.avatar{width:70px;height:70px;border-radius:50%;background:linear-gradient(160deg,#d9c3a9,#9a8268)}
.avatar.dark{background:linear-gradient(160deg,#8a7565,#3f342d)}
.author-name{font-style:italic;font-size:12px;color:var(--gold)}
.rating{display:flex;align-items:center;gap:6px;margin-top:10px;margin-left:12px;font-size:12px;font-style:italic;color:var(--plum)}
.stars{display:flex;gap:1px}
.stars span{width:16px;height:14px;background:var(--plum);display:flex;align-items:center;justify-content:center;color:var(--white);font-size:10px;font-style:normal}
.slider-arrow{position:absolute;top:192px}

/* games */
.games{position:absolute;left:0;top:1960px;width:1200px;height:532px;background:var(--plum)}
.games .section-title{position:absolute;top:82px;left:0;right:0;color:var(--white)}
.game-card{position:absolute;top:155px;width:218px;height:288px;background:var(--white);text-align:center;padding:4px}
.game-photo{height:150px}
.game-card h3{font-family:"Raleway",sans-serif;font-weight:500;font-size:14px;color:var(--ink);margin-top:18px}
.game-card p{font-size:10.5px;line-height:18px;color:#666;margin:8px 14px 0}
.game-card .btn-outline{border-color:var(--gold);color:var(--gold);margin-top:12px;font-size:9px;padding:8px 10px}

/* footer */
.site-footer{position:absolute;left:0;top:2492px;width:1200px;height:277px;background:var(--soft)}
.footer-brand{position:absolute;left:130px;top:68px;display:flex;align-items:center;gap:12px}
.copyright{position:absolute;left:160px;top:170px;font-size:11px;color:var(--ink)}
.footer-col{position:absolute;top:50px}
.footer-col h4{font-family:"Raleway",sans-serif;font-weight:500;font-size:15px;color:var(--ink);letter-spacing:.3px}
.contact-line{display:flex;gap:12px;font-size:11.5px;line-height:20px;color:#555;margin-top:14px}
.contact-line:first-of-type{margin-top:20px}
.contact-line svg{flex:none;margin-top:3px}
.links{list-style:none;margin-top:18px}
.links li{font-size:10.5px;color:#555;line-height:25px}
.news-text{font-size:11px;line-height:19px;color:#555;margin-top:18px;width:260px}
.field{width:154px;height:40px;background:var(--white);border:1px solid #e6e6e6;font-size:10px;color:#555;padding:12px 14px;margin-top:12px}
.subscribe-row{display:flex;margin-top:8px}
.subscribe-row .field{margin-top:0}
.subscribe{width:92px;height:40px;background:var(--gold);color:var(--white);font-size:10px;font-weight:600;text-align:center;line-height:40px}
</style>
</head>
<body>

<header class="site-header">
  <div class="brand">
    <span class="brand-mark"></span>
    <span class="brand-name">Studio Pelican</span>
  </div>
  <div class="top-contact">
    <svg width="22" height="22" viewBox="0 0 22 22"><circle cx="11" cy="11" r="10" fill="none" stroke="#a8426f" stroke-width="1.5"/><path d="M7.5 6.5l2 0 1 2.5-1.2 1a6 6 0 0 0 2.7 2.7l1-1.2 2.5 1v2a1 1 0 0 1-1 1A8 8 0 0 1 6.5 7.5a1 1 0 0 1 1-1z" fill="#a8426f"/></svg>
    <span>Call Us : <b>555-310-4872</b></span>
    <div class="socials"><span></span><span></span><span></span><span></span></div>
  </div>
  <nav class="main-nav">
    <a class="active" href="#">HOME</a>
    <a href="#">ABOUT US</a>
    <a href="#">SERVICES</a>
    <a href="#">TESTIMONIALS</a>
    <a href="#">BLOG</a>
    <a href="#">CONTACT US</a>
  </nav>
</header>

<section class="hero">
  <div class="hero-photo" role="img" aria-label="Photo of a student writing notes at a library desk with open books"></div>
  <div class="hero-copy">
    <div class="hero-kicker">LANGUAGE TUTORING FOR SCHOLARS</div>
    <h1 class="hero-title">FRENCH LANGUAGE</h1>
    <p class="hero-text">Adipiscing elit, sed do eiusmod tempor incididunt ut labore et dolore magna aliqua. Ut enim ad minim...</p>
    <a class="btn-outline" href="#">LEARN MORE INFORMATION</a>
  </div>
  <div class="hero-dots"><span></span><span class="on"></span><span></span><span></span></div>
</section>

<section class="services">
  <h2 class="section-title">EDUCATIONAL <b>SERVICES</b></h2>

  <article class="service-card" style="left:131px">
    <div class="service-icon gold"><svg viewBox="0 0 80 80"><g fill="none" stroke="#fff" stroke-width="2"><path d="M20 27h17a3 3 0 0 1 3 2v26a4 4 0 0 0-3-2H20z"/><path d="M60 27H43a3 3 0 0 0-3 2v26a4 4 0 0 1 3-2h17z"/><path d="M25 34h10M25 40h10M25 46h10M45 34h10M45 40h10M45 46h10" stroke-width="1.5"/></g></svg></div>
    <h3>NEMO ENIM&nbsp; VOLUPTATEM</h3>
    <p>Lorem ipsum dolor sit amet, consecteadipiscing elit, sed do eiusmod tempor incididunt ut labore et dolore magna aliqua...</p>
    <a class="more" href="#">LEARN MORE &#10141;</a>
  </article>

  <article class="service-card" style="left:452px">
    <div class="service-icon plum"><svg viewBox="0 0 80 80"><g fill="none" stroke="#fff" stroke-width="2"><path d="M25 22h21l7 7v29H25z"/><path d="M30 32h12M30 38h10M30 44h8" stroke-width="1.5"/><path d="M60 32L46 48l-4 6 6-3 15-16z"/></g></svg></div>
    <h3>NEMO ENIM&nbsp; VOLUPTATEM</h3>
    <p>Lorem ipsum dolor sit amet, consecteadipiscing elit, sed do eiusmod tempor incididunt ut labore et dolore magna aliqua...</p>
    <a class="more plum" href="#">LEARN MORE &#10141;</a>
  </article>

  <article class="service-card" style="left:772px">
    <div class="service-icon plum"><svg viewBox="0 0 80 80"><g fill="none" stroke="#fff" stroke-width="2"><circle cx="40" cy="40" r="18"/><ellipse cx="40" cy="40" rx="8" ry="18"/><path d="M22 40h36M24 31h32M24 49h32"/></g></svg></div>
    <h3>NEMO ENIM&nbsp; VOLUPTATEM</h3>
    <p>Lorem ipsum dolor sit amet, consecteadipiscing elit, sed do eiusmod tempor incididunt ut labore et dolore magna aliqua...</p>
    <a class="more plum" href="#">LEARN MORE &#10141;</a>
  </article>
</section>

<section class="tutoring">
  <h2 class="tutoring-title">TUTORING FOR <b>SCHOLARS</b></h2>
  <ul class="tick-list">
    <li><svg width="12" height="10" viewBox="0 0 12 10"><path d="M1 5l3.5 3.5L11 1.5" fill="none" stroke="#fff" stroke-width="2"/></svg>Eiusmod tempor incididunt ut labore et dolore magna aliqua. Ut enim ad minim veniam, quis nostrud exercitation ullamco laboris nisi ut aliquip</li>
    <li><svg width="12" height="10" viewBox="0 0 12 10"><path d="M1 5l3.5 3.5L11 1.5" fill="none" stroke="#fff" stroke-width="2"/></svg>Eiusmod tempor incididunt ut labore et dolore magna aliqua. Ut enim ad minim veniam, quis nostrud exercitation ullamco laboris nisi ut aliquip</li>
    <li><svg width="12" height="10" viewBox="0 0 12 10"><path d="M1 5l3.5 3.5L11 1.5" fill="none" stroke="#fff" stroke-width="2"/></svg>Eiusmod tempor incididunt ut labore et dolore magna aliqua. Ut enim ad minim veniam, quis nostrud exercitation ullamco laboris nisi ut aliquip</li>
  </ul>
  <a class="btn-outline" href="#">LEARN MORE INFORMATION</a>

  <div class="video">
    <div class="video-frame" role="img" aria-label="Video still of students working together at computers in a classroom"></div>
    <svg class="video-play" width="60" height="60" viewBox="0 0 60 60"><circle cx="30" cy="30" r="27" fill="rgba(0,0,0,.25)" stroke="#fff" stroke-width="3"/><path d="M24 19l17 11-17 11z" fill="none" stroke="#fff" stroke-width="3" stroke-linejoin="round"/></svg>
    <svg class="video-bar" width="440" height="26" viewBox="0 0 440 26">
      <rect width="440" height="26" fill="#fff"/>
      <path d="M14 9l7 4-7 4z" fill="#333"/>
      <text x="44" y="16" font-family="Open Sans, sans-serif" font-size="7" fill="#333">00:00 / 01:01</text>
      <rect x="114" y="12" width="230" height="2" fill="#ccc"/>
      <rect x="114" y="12" width="90" height="2" fill="#c0392b"/>
      <path d="M372 10h3l4-3v12l-4-3h-3z" fill="#333"/>
      <rect x="388" y="12" width="36" height="2" fill="#c0392b"/>
    </svg>
  </div>
</section>

<section class="testimonials">
  <h2 class="section-title">SCHOLARS <b>TESTIMONIALS</b></h2>
  <svg class="slider-arrow" style="left:80px" width="20" height="60" viewBox="0 0 20 60"><path d="M18 2L3 30l15 28" fill="none" stroke="#cfcfcf" stroke-width="2"/></svg>
  <svg class="slider-arrow" style="left:1100px" width="20" height="60" viewBox="0 0 20 60"><path d="M2 2l15 28L2 58" fill="none" stroke="#cfcfcf" stroke-width="2"/></svg>

  <blockquote class="quote" style="left:133px">
    <p>Remy knows exactly how to accomplish and complete the sale, no matter how difficult. He is intuitive, experienced, professional, and knows how it all works. In my case, with Northbank, he had to represent my interest yet get it all done in the best way possible within the time</p>
    <div class="author">
      <div class="avatar" role="img" aria-label="Portrait photo of a smiling scholar"></div>
      <div>
        <div class="author-name">Remy Tallovin / Our Scholar</div>
        <div class="rating"><div class="stars"><span>★</span><span>★</span><span>★</span><span>★</span><span>★</span></div>(88 reviews)</div>
      </div>
    </div>
  </blockquote>

  <blockquote class="quote" style="left:656px">
    <p>Remy knows exactly how to accomplish and complete the sale, no matter how difficult. He is intuitive, experienced, professional, and knows how it all works. In my case, with Northbank, he had to represent my interest yet get it all done in the best way possible within the time</p>
    <div class="author">
      <div class="avatar dark" role="img" aria-label="Portrait photo of a smiling scholar"></div>
      <div>
        <div class="author-name">Remy Tallovin / Our Scholar</div>
        <div class="rating"><div class="stars"><span>★</span><span>★</span><span>★</span><span>★</span><span>★</span></div>(88 reviews)</div>
      </div>
    </div>
  </blockquote>
</section>

<section class="games">
  <h2 class="section-title">LANGUAGE <b>CARDS GAMES</b></h2>

  <article class="game-card" style="left:132px">
    <div class="game-photo" role="img" aria-label="Photo of colourful game cards spread on a green table" style="background:linear-gradient(135deg,#2e9a5a,#e6b9c4 60%,#f1e7e2)"></div>
    <h3>CARD MATCH</h3>
    <p>Sequi nesciunt. Neque quisquam est, qui dolorem ipsum...</p>
    <a class="btn-outline" href="#">LEARN MORE</a>
  </article>

  <article class="game-card" style="left:372px">
    <div class="game-photo" role="img" aria-label="Photo of a falling row of dominos on a dark table" style="background:linear-gradient(160deg,#1b1410,#5a3a22 55%,#8a6040)"></div>
    <h3>DOMINOS</h3>
    <p>Sequi nesciunt. Neque quisquam est, qui dolorem ipsum...</p>
    <a class="btn-outline" href="#">LEARN MORE</a>
  </article>

  <article class="game-card" style="left:612px">
    <div class="game-photo" role="img" aria-label="Photo of hands joining large puzzle pieces" style="background:linear-gradient(135deg,#4a5058,#9ba3aa 50%,#7fa25a)"></div>
    <h3>PUZZLE</h3>
    <p>Sequi nesciunt. Neque quisquam est, qui dolorem ipsum...</p>
    <a class="btn-outline" href="#">LEARN MORE</a>
  </article>

  <article class="game-card" style="left:852px">
    <div class="game-photo" role="img" aria-label="Photo of a family playing a card game together at home" style="background:linear-gradient(135deg,#c89a78,#e8d4c2 55%,#8f6a55)"></div>
    <h3>HAPPY FAMILY CARDS</h3>
    <p>Sequi nesciunt. Neque quisquam est, qui dolorem ipsum...</p>
    <a class="btn-outline" href="#">LEARN MORE</a>
  </article>
</section>

<footer class="site-footer">
  <div class="footer-brand">
    <span class="brand-mark"></span>
    <span class="brand-name">Studio Pelican</span>
  </div>
  <div class="copyright">2017 © STUDIOPELICAN.</div>

  <div class="footer-col" style="left:400px">
    <h4>CONTACT US</h4>
    <div class="contact-line"><svg width="12" height="15" viewBox="0 0 12 15"><path d="M6 14S1 8.5 1 5.5a5 5 0 0 1 10 0C11 8.5 6 14 6 14z" fill="#e0ad4a"/><circle cx="6" cy="5.5" r="1.8" fill="#fff"/></svg><span>Studiopelican P.O. Box 2210<br>Street Name , City-4535</span></div>
    <div class="contact-line"><svg width="12" height="14" viewBox="0 0 12 14"><path d="M2 1h3l1.2 3-1.6 1.3a7 7 0 0 0 3.4 3.4L9.3 7 12 8.2V11a1.5 1.5 0 0 1-1.5 1.5A10 10 0 0 1 .5 2.5 1.5 1.5 0 0 1 2 1z" fill="#e0ad4a"/></svg><span>Phone: 555-310-4872<br>Fax: 555-310-4873</span></div>
    <div class="contact-line"><svg width="12" height="10" viewBox="0 0 12 10"><rect x="0.5" y="1" width="11" height="8" fill="#e0ad4a"/><path d="M1 1.5l5 4 5-4" fill="none" stroke="#fff" stroke-width="1"/></svg><span>Email: hello@studiopelican.example</span></div>
  </div>

  <div class="footer-col" style="left:668px">
    <h4>QUICK LINKS</h4>
    <ul class="links">
      <li>Home</li><li>About Us</li><li>Our Services</li><li>Testimonials</li><li>Blog</li><li>Contact Us</li>
    </ul>
  </div>

  <div class="footer-col" style="left:821px">
    <h4>SIGN UP FOR NEWSLETTER</h4>
    <p class="news-text">Get the latest updates on our courses and events: Notify Me</p>
    <div class="field" style="width:246px">Enter Name</div>
    <div class="subscribe-row">
      <div class="field">Enter Email</div>
      <div class="subscribe">SUBSCRIBE</div>
    </div>
  </div>
</footer>

</body>
</html>
```